Thank you for shopping with us business card

We would like a thank you card for our rebranded business. We used to be "Brindle Goods" but are now "Marlow Finds. Old thank you card and new logo will be attached for reference. New thank you card does not have to be same design as old thank you card, but please use new logo.
Shopmart URL is now marlowfinds.shopmart.example
Instagram is @Marlow_Finds
Email is marlowfinds@mailbox.example
Thank you!

Contact Information for Business Card

Shopmart site, email, Instagram

```html
<!DOCTYPE html>
<html lang="en">
<head>
<meta charset="utf-8">
<title>Marlow Finds – Thank You Card</title>
<link href="https://fonts.googleapis.com/css2?family=Montserrat:wght@400;500;700;800&display=swap" rel="stylesheet">
<style>
  :root {
    --teal: #159fc1;
    --teal-deep: #0f8fb1;
    --teal-light: #22aacb;
    --white: #ffffff;
    --backdrop: #3b3b3d;
  }
  * { margin: 0; padding: 0; box-sizing: border-box; }
  html, body {
    width: 1200px; height: 1200px; overflow: hidden;
    background: var(--backdrop);
    font-family: "Montserrat", sans-serif;
  }
  .stage {
    width: 1200px; height: 1200px;
    display: flex; align-items: center; justify-content: center;
  }
  .thank-you-card {
    position: relative;
    width: 1000px; height: 700px;
    background: var(--teal);
    overflow: hidden;
    color: var(--white);
    box-shadow: 0 20px 50px rgba(0,0,0,.45);
  }
  .card-pattern {
    position: absolute; inset: 0;
    background: linear-gradient(135deg, var(--teal-light) 0%, var(--teal) 50%, var(--teal-deep) 100%);
  }
  .brand {
    position: absolute; left: 205px; top: 95px;
    display: flex; align-items: center; height: 180px;
  }
  .brand-mark {
    width: 120px; height: 120px; border-radius: 50%;
    background: var(--white);
  }
  .brand-divider {
    width: 2px; height: 160px; background: var(--white);
    margin: 0 32px 0 38px;
  }
  .brand-name {
    font-weight: 700; font-size: 46px; line-height: 1.08;
    letter-spacing: -0.5px; text-transform: uppercase;
    color: var(--white);
  }
  .thanks-band {
    position: absolute; left: 0; right: 0; top: 300px; height: 86px;
    background: var(--white);
    display: flex; align-items: center;
    padding-left: 205px;
  }
  .thanks-heading {
    font-weight: 800; font-size: 40px; letter-spacing: 0.3px;
    color: var(--teal); text-transform: uppercase;
    white-space: nowrap;
  }
  .thanks-message {
    position: absolute; left: 250px; top: 412px; width: 720px;
    font-weight: 500; font-size: 32px; line-height: 1.3;
    letter-spacing: 0.3px; white-space: nowrap;
  }
  .contact-rule {
    position: absolute; left: 250px; right: 55px; top: 578px;
    height: 1px; background: rgba(255,255,255,.55);
  }
  .contact-list {
    position: absolute; left: 250px; right: 30px; top: 602px;
    display: flex; justify-content: space-between; gap: 18px; list-style: none;
    font-size: 14px; font-weight: 500; letter-spacing: 0.1px;
    white-space: nowrap;
  }
  .contact-item { display: flex; align-items: center; gap: 8px; }
  .contact-icon { width: 22px; height: 22px; flex: none; }
</style>
</head>
<body>
<main class="stage">
  <article class="thank-you-card">
    <div class="card-pattern" role="img" aria-label="Faint repeating brand pattern across the teal background"></div>

    <header class="brand">
      <div class="brand-mark" aria-hidden="true"></div>
      <div class="brand-divider"></div>
      <h1 class="brand-name">Marlow<br>Finds</h1>
    </header>

    <div class="thanks-band">
      <h2 class="thanks-heading">Thank you for your purchase!</h2>
    </div>

    <p class="thanks-message">Your purchase made my day and I<br>hope this package brightens yours.<br>Please come back and leave a review!</p>

    <div class="contact-rule"></div>

    <ul class="contact-list">
      <li class="contact-item">
        <svg class="contact-icon" viewBox="0 0 24 24" aria-hidden="true"><circle cx="12" cy="12" r="11" fill="#fff"/></svg>
        marlowfinds.shopmart.example
      </li>
      <li class="contact-item">
        <svg class="contact-icon" viewBox="0 0 24 24" aria-hidden="true"><circle cx="12" cy="12" r="11" fill="#fff"/></svg>
        @Marlow_Finds
      </li>
      <li class="contact-item">
        <svg class="contact-icon" viewBox="0 0 24 24" aria-hidden="true">
          <circle cx="12" cy="12" r="11" fill="#fff"/>
          <rect x="6.5" y="8" width="11" height="8" fill="none" stroke="#159fc1" stroke-width="1.4"/>
          <path d="M6.5 8 L12 12.5 L17.5 8" fill="none" stroke="#159fc1" stroke-width="1.4"/>
        </svg>
        marlowfinds@mailbox.example
      </li>
    </ul>
  </article>
</main>
</body>
</html>
```